Webpage needed for a new legal recruitment/headhunting companyi

I would like a professional and sharp looking website to showcase a new legal headhunting/recruitment company called Mosswick. The logo for the company is attached.

I like the following websites:
http://www.brindletalent.co.uk/
(For the general style and layout- although photographs of the team will be difficult as we don't have one yet!;-))

http://qorv.co.uk/
I like the style of the photographs etc on this one.

NB the pictures attached below are for information only- I don't think I would be able to use any of them...

Hope you can help!
Many thanks

Industry/Entity Type

Legal

```html
<!DOCTYPE html>
<html lang="en">
<head>
<meta charset="utf-8">
<title>Mosswick Legal Recruitment</title>
<link href="https://fonts.googleapis.com/css2?family=Open+Sans:wght@400;600&display=swap" rel="stylesheet">
<style>
:root{
  --purple:#4e2d6d;
  --purple-dark:#3d1f5a;
  --page:#f0f0f2;
  --grey-band:#e6e6e9;
  --ink:#222;
  --muted:#555;
  --footer:#25222a;
  --footer-text:#cfcfd4;
  --field:#c9c9cc;
}
*{margin:0;padding:0;box-sizing:border-box}
html,body{width:763px;height:1200px;overflow:hidden}
body{position:relative;background:var(--page);font-family:"Open Sans",Arial,sans-serif;color:var(--ink)}
.abs{position:absolute}
.brand{left:117px;top:22px;display:flex;align-items:center;gap:8px;color:var(--purple);font-size:30px;font-weight:400;letter-spacing:.5px}
.brand-dot{width:14px;height:14px;border-radius:50%;background:var(--purple)}
.search{left:444px;top:38px;width:164px;height:24px;background:#fff;border:1px solid #d6d6d9;font-size:8px;color:#aaa;padding:7px 7px}
.search-btn{left:615px;top:38px;width:34px;height:24px;background:#111;display:flex;align-items:center;justify-content:center}
.nav{left:0;top:83px;width:763px;height:26px;background:var(--purple)}
.nav ul{list-style:none;display:flex;margin-left:110px;height:26px}
.nav li{color:#fff;font-size:7.5px;line-height:26px;padding:0 9.5px}
.nav li.active{background:#e4e4e6;color:#222;padding:0 12px}
.hero{left:0;top:109px;width:763px;height:301px;background:linear-gradient(100deg,#3b3a3f 0%,#c9b8a3 25%,#e6e2da 45%,#7d8c95 65%,#3b3a40 100%)}
.hero-caption{left:118px;top:272px;width:322px;height:88px;background:rgba(90,90,95,.6);padding:12px 10px;color:#fff}
.hero-caption h2{font-size:12.5px;font-weight:400;margin-bottom:9px}
.hero-caption p{font-size:7px;line-height:16px;padding-left:3px}
.hero-arrow{top:273px;width:12px;height:12px;border-radius:50%;background:rgba(60,60,60,.7)}
.dots{left:355px;top:394px;display:flex;gap:5px}
.dots span{width:7px;height:7px;border-radius:50%;background:rgba(200,200,200,.7)}
.dots span.on{background:var(--purple)}
.welcome{left:0;top:410px;width:763px;height:190px;background:#fff;border-bottom:1px solid #ccc}
.welcome h1{position:absolute;left:115px;top:21px;font-size:13.5px;font-weight:400}
.rule{position:absolute;left:115px;top:43px;width:534px;height:1px;background:#ddd}
.rule i{position:absolute;left:0;top:0;width:117px;height:1px;background:var(--purple)}
.welcome p{position:absolute;left:115px;top:55px;width:535px;font-size:7px;line-height:13px;color:#333}
.welcome ul{position:absolute;left:215px;top:110px;list-style:none}
.welcome li{font-size:7px;line-height:16.4px;color:#333}
.welcome li::before{content:"\270E";margin-right:4px;color:#666}
.features{left:0;top:600px;width:763px;height:353px;background:var(--grey-band)}
.card{position:absolute;top:18px;width:158px;height:186px;box-shadow:0 1px 2px rgba(0,0,0,.2)}
.card-icon{height:102px;background:#fff;display:flex;align-items:center;justify-content:center}
.card-body{height:84px;background:var(--purple);color:#fff;padding:10px 12px}
.card-body h3{font-size:9px;font-weight:600;margin-bottom:10px}
.card-body p{font-size:7px;line-height:13px}
.panel{position:absolute;top:238px;width:260px}
.panel-head{height:24px;background:#fff;border-bottom:2px solid #bbb;display:flex;align-items:center;justify-content:space-between;padding:0 7px}
.panel-head h4{font-size:9px;font-weight:600}
.arrows{display:flex;gap:5px}
.arrows span{width:11px;height:10px;display:flex;align-items:center;justify-content:center;color:#fff;font-size:8px;line-height:1}
.arrows .prev{background:#222}.arrows .next{background:var(--purple)}
.panel-body{margin-top:7px;height:57px;background:#fff;box-shadow:0 1px 2px rgba(0,0,0,.15);position:relative}
.news-thumb{position:absolute;left:0;top:0;width:96px;height:57px;background:linear-gradient(135deg,#5a5a5a,#c9c4bb)}
.news-date{position:absolute;left:3px;top:2px;width:20px;height:17px;background:var(--purple);color:#fff;font-size:5.5px;text-align:center;line-height:8px;padding-top:1px}
.news-text{position:absolute;left:100px;top:6px;width:150px}
.news-text h5{font-size:7.5px;font-weight:400;margin-bottom:3px}
.news-text p,.testi p{font-size:6.2px;line-height:10px;color:#444}
.testi-photo{position:absolute;left:7px;top:6px;width:44px;height:44px;background:linear-gradient(160deg,#b99a86,#6e5446)}
.testi{position:absolute;left:59px;top:9px;width:195px}
.footer{left:0;top:953px;width:763px;height:247px;background:var(--footer);color:var(--footer-text)}
.footer h4{position:absolute;top:21px;font-size:10px;font-weight:400;color:#e4e4e6}
.field{position:absolute;left:116px;width:149px;background:var(--field);border:2px solid #9a9a9e;border-radius:2px;font-size:7.5px;color:#666;padding:3px 5px}
.submit{position:absolute;left:116px;top:142px;width:47px;height:19px;background:var(--purple-dark);color:#fff;font-size:7px;text-align:center;line-height:19px;border-radius:2px}
.map{position:absolute;left:315px;top:38px;width:109px;height:72px;border:1px solid #888;background:linear-gradient(180deg,#8fb3d9 0%,#7f9276 45%,#3f8fb0 75%,#2f6f9c 100%)}
.loc{position:absolute;left:314px;top:118px;font-size:7px;line-height:16.4px;color:#ddd}
.social{position:absolute;left:491px;list-style:none}
.social li{display:flex;align-items:center;gap:7px;height:20px;margin-bottom:7px;font-size:7.5px}
.social i{width:20px;height:20px;border-radius:3px;display:block}
.footer-rule{position:absolute;left:115px;top:182px;width:534px;height:1px;background:#3d3a42}
.footer-links{position:absolute;left:0;top:196px;width:763px;text-align:center;font-size:7.5px}
.footer-links span{margin:0 7px}
.copy{position:absolute;left:0;top:223px;width:763px;text-align:center;font-size:6px}
</style>
</head>
<body>
<header>
  <div class="abs brand"><span class="brand-dot"></span>Mosswick</div>
  <div class="abs search">Search...</div>
  <div class="abs search-btn"><svg width="11" height="11" viewBox="0 0 12 12"><circle cx="5" cy="5" r="3.6" fill="none" stroke="#fff" stroke-width="1.6"/><line x1="7.6" y1="7.6" x2="11" y2="11" stroke="#fff" stroke-width="1.8"/></svg></div>
  <nav class="abs nav"><ul>
    <li class="active">HOME</li><li>SERVICES</li><li>CANDIDATES</li><li>CLIENTS</li><li>TEAM</li><li>ADVICE</li><li>CONTACT US</li>
  </ul></nav>
</header>

<section class="abs hero" role="img" aria-label="Photo of legal professionals in a business meeting"></section>
<div class="abs hero-arrow" style="left:8px"></div>
<div class="abs hero-arrow" style="left:742px"></div>
<div class="abs hero-caption">
  <h2>SLIDE BACKGROUNDMAURIS SUSCIPIT</h2>
  <p>Fusce auctor felis non placerat sagittis. Nulla lacus mauris, accumsan a dapibus nec, adipiscing et enim. Aliquam ac arcu quis tortor tempus accumsan non at ligula.</p>
</div>
<div class="abs dots"><span></span><span></span><span class="on"></span><span></span></div>

<section class="abs welcome">
  <h1>Welcome To Mosswick</h1>
  <div class="rule"><i></i></div>
  <p>Quisque vestibulum posuere neque, ut viverra massa dignissim tincidunt. Class aptent taciti sociosqu ad litora torquent per conubia nostra, per inceptos himenaeos. Curabitur quis enim nunc, nec posuere velit. mollis interdum. Morbi leo risus Quisque vestibulum posuere neque, ut viverra massa dignissim tincidunt. Class aptent taciti sociosqu ad litora torquent per conubia nostra, per inceptos himenaeos. Curabitur quis enim nunc, nec posuere velit. mollis interdum. Morbi leo risus</p>
  <ul>
    <li>Phasellus dictum placerat pellentesque</li>
    <li>Etiam porta sem malesuada magna mollis euismod</li>
    <li>Nhasellus dictum placerat pellentesque</li>
    <li>Felis orci hendrerit a pulvinar et gravida</li>
  </ul>
</section>

<section class="abs features">
  <div class="card" style="left:122px">
    <div class="card-icon"><svg width="40" height="40" viewBox="0 0 40 40" fill="none" stroke="#333" stroke-width="2.2"><circle cx="31" cy="7" r="4.5"/><circle cx="7" cy="20" r="4.5"/><circle cx="31" cy="33" r="4.5"/><line x1="11" y1="18" x2="27" y2="9"/><line x1="11" y1="22" x2="27" y2="31"/></svg></div>
    <div class="card-body"><h3>Successes</h3><p>Praesent vehicula eros id eleifend praesent tristique porta suscipit curae suspendise</p></div>
  </div>
  <div class="card" style="left:302px">
    <div class="card-icon"><svg width="38" height="38" viewBox="0 0 38 38" fill="none" stroke="#333" stroke-width="2.2"><circle cx="19" cy="19" r="16"/><circle cx="19" cy="19" r="7"/><line x1="19" y1="3" x2="19" y2="12"/><line x1="19" y1="26" x2="19" y2="35"/><line x1="3" y1="19" x2="12" y2="19"/><line x1="26" y1="19" x2="35" y2="19"/></svg></div>
    <div class="card-body"><h3>Support</h3><p>Praesent vehicula eros id eleifend praesent tristique porta suscipit curae suspendise</p></div>
  </div>
  <div class="card" style="left:481px">
    <div class="card-icon"><svg width="38" height="38" viewBox="0 0 38 38" fill="none" stroke="#333" stroke-width="2.2"><circle cx="26" cy="11" r="8"/><line x1="20" y1="17" x2="5" y2="32"/><line x1="5" y1="32" x2="9" y2="36"/><line x1="9" y1="28" x2="12" y2="31"/></svg></div>
    <div class="card-body"><h3>Real Salaries</h3><p>Praesent vehicula eros id eleifend praesent tristique porta suscipit curae suspendise</p></div>
  </div>

  <div class="panel" style="left:115px">
    <div class="panel-head"><h4>Latest News</h4><div class="arrows"><span class="prev">&#8592;</span><span class="next">&#8594;</span></div></div>
    <div class="panel-body">
      <div class="news-thumb" role="img" aria-label="Photo of a CV document and pen"></div>
      <div class="news-date">15<br>MAR</div>
      <div class="news-text"><h5>Aenean Tincidunt Eros At Luctus</h5><p>Integer facilisis pharetra risus eget auctor. Nullam viverra dapibus tellus, sit amet cursus turpis vulputate consectetur.</p></div>
    </div>
  </div>
  <div class="panel" style="left:389px">
    <div class="panel-head"><h4>Testmonials</h4><div class="arrows"><span class="prev">&#8592;</span><span class="next">&#8594;</span></div></div>
    <div class="panel-body">
      <div class="testi-photo" role="img" aria-label="Portrait photo of a client"></div>
      <div class="testi"><p>Integer facilisis pharetra risus eget auctor. Nullam viverra dapibus tellus, sit amet cursus turpis vulputate consectetur.</p></div>
    </div>
  </div>
</section>

<footer class="abs footer">
  <h4 style="left:115px">Quick Contact</h4>
  <div class="field" style="top:39px;height:19px">Name</div>
  <div class="field" style="top:66px;height:19px">Email Address</div>
  <div class="field" style="top:93px;height:41px">Comments or Questions..</div>
  <div class="submit">SUBMIT</div>

  <h4 style="left:306px">Our Location</h4>
  <div class="map" role="img" aria-label="Photo of a coastal town and harbour"></div>
  <div class="loc">Lorem Ipsm ,Street Name, City- 123 456<br>Phone : 123 456 789<br>Email : info@mosswick.co.uk</div>

  <h4 style="left:479px">Connect Us</h4>
  <ul class="social" style="top:42px">
    <li style="color:#f08a24"><i style="background:#f08a24"></i>RSS Feed</li>
    <li style="color:#4b67a8"><i style="background:#3b5998"></i>Circlebook</li>
    <li style="color:#3fa9e6"><i style="background:#2fa9e6"></i>Chirper</li>
    <li style="color:#e04a3a"><i style="background:#d9402f"></i>Orbit Plus</li>
  </ul>

  <div class="footer-rule"></div>
  <div class="footer-links"><span>Terms of Service</span><span>Privacy Policy</span><span>Events</span><span>Contact</span><span>Blog</span><span>Sitemap</span></div>
  <div class="copy">copyright @ 2014 Mosswick .all right reserved.</div>
</footer>
</body>
</html>
```